Corporate ppt for clients and partners /knowledge in German is important

We need to better design our ppt's that are used to present our firm to clients. Attached is the version that we currently use to explain our services to potential clients.
I would like to see a design that communicates clarity, integrity and uniqueness.

```html
<!DOCTYPE html>
<html lang="de">
<head>
<meta charset="utf-8">
<title>Leistungsübersicht</title>
<link rel="stylesheet" href="https://fonts.googleapis.com/css2?family=Exo+2:wght@400;500;600&display=swap">
<style>
  :root {
    --blue: #1a6ab6;
    --blue-deep: #0b5aa5;
    --header-dark: #0a3fb0;
    --header-light: #2fa8f0;
    --green: #2f8a55;
    --lime: #9db927;
    --orange: #ee6a2b;
    --text: #333a40;
    --white: #ffffff;
  }
  html, body {
    margin: 0;
    padding: 0;
    width: 1200px;
    height: 900px;
    overflow: hidden;
    background: var(--white);
  }
  .slide {
    position: relative;
    width: 1200px;
    height: 900px;
    overflow: hidden;
    font-family: "Exo 2", "Segoe UI", sans-serif;
    background: var(--white);
  }
  .hero {
    position: absolute;
    left: 0;
    top: 0;
    width: 1200px;
    height: 270px;
    background:
      radial-gradient(circle at 560px 110px, rgba(150,220,255,0.75) 0, rgba(80,170,255,0.35) 120px, rgba(0,0,0,0) 230px),
      linear-gradient(100deg, var(--header-dark) 0%, #1577e0 45%, var(--header-light) 75%, #1564d8 100%);
  }
  .hero-edge {
    position: absolute;
    left: 0;
    top: 262px;
    width: 1200px;
    height: 56px;
  }
  .services {
    position: absolute;
    left: 53px;
    top: 342px;
    margin: 0;
    padding: 0;
    list-style: none;
  }
  .service {
    display: flex;
    align-items: center;
    height: 76px;
    margin-bottom: 50px;
  }
  .service-icon {
    width: 74px;
    height: 74px;
    flex: none;
    margin-right: 25px;
  }
  .service-title {
    margin: 0 0 2px;
    font-size: 26px;
    font-weight: 500;
    line-height: 1.15;
  }
  .service-text {
    margin: 0;
    font-size: 18px;
    font-weight: 400;
    color: var(--text);
  }
  .service--pentest .service-title { color: var(--blue); }
  .service--appsec .service-title { color: var(--green); }
  .service--research .service-title { color: var(--lime); }
  .service--training .service-title { color: var(--orange); }
  .footer {
    position: absolute;
    left: 0;
    bottom: 0;
    width: 1200px;
    height: 36px;
    background: var(--blue-deep);
  }
  .footer-copy {
    position: absolute;
    left: 11px;
    top: 7px;
    margin: 0;
    color: var(--white);
    font-size: 18px;
    font-weight: 500;
  }
  .brand {
    position: absolute;
    right: 18px;
    bottom: 44px;
    display: flex;
    align-items: center;
    gap: 8px;
    color: var(--blue-deep);
    font-size: 22px;
    font-weight: 600;
  }
  .brand-dot {
    width: 14px;
    height: 14px;
    border-radius: 50%;
    background: var(--blue-deep);
  }
</style>
</head>
<body>
<main class="slide">
  <div class="hero" role="img" aria-label="Blaue Technologie-Illustration mit Leiterbahnen und leuchtendem Sicherheitsschloss"></div>

  <svg class="hero-edge" viewBox="0 0 1200 56" aria-hidden="true">
    <path d="M0 0 H1200 V8 H215 C190 8 180 22 170 50 C160 22 150 8 125 8 H0 Z" fill="var(--blue-deep)"/>
  </svg>

  <ul class="services">
    <li class="service service--pentest">
      <svg class="service-icon" viewBox="0 0 74 74" aria-hidden="true">
        <circle cx="37" cy="37" r="37" fill="var(--blue)"/>
        <g fill="none" stroke="var(--white)" stroke-width="2.6" stroke-linecap="round">
          <path d="M30 56 A20 20 0 1 1 44 56"/>
          <path d="M31 50 A14 14 0 1 1 43 50"/>
          <path d="M33 44 A8 8 0 1 1 41 44"/>
          <path d="M37 30 V40"/>
        </g>
      </svg>
      <div>
        <h2 class="service-title">Penetration Test</h2>
        <p class="service-text">Penetrationstests und Sicherheitsberatung</p>
      </div>
    </li>
    <li class="service service--appsec">
      <svg class="service-icon" viewBox="0 0 74 74" aria-hidden="true">
        <circle cx="37" cy="37" r="37" fill="var(--green)"/>
        <circle cx="37" cy="37" r="24" fill="none" stroke="var(--white)" stroke-width="2.6"/>
        <g fill="var(--white)">
          <circle cx="30" cy="32" r="5"/>
          <path d="M20 50 C20 40 40 40 40 50 Z"/>
          <circle cx="45" cy="34" r="4"/>
          <path d="M37 50 C37 42 53 42 53 50 Z"/>
        </g>
      </svg>
      <div>
        <h2 class="service-title">Applikationssicherheit</h2>
        <p class="service-text">Reverse Engineering &amp; Source Code Review</p>
      </div>
    </li>
    <li class="service service--research">
      <svg class="service-icon" viewBox="0 0 74 74" aria-hidden="true">
        <circle cx="37" cy="37" r="37" fill="var(--lime)"/>
        <circle cx="33" cy="33" r="11" fill="none" stroke="var(--white)" stroke-width="4"/>
        <path d="M41 41 L53 53" stroke="var(--white)" stroke-width="6" stroke-linecap="round"/>
      </svg>
      <div>
        <h2 class="service-title">Forschung &amp; Entwicklung</h2>
        <p class="service-text">Eigenes IT-Forschungslabor zur Kompetenzsicherung</p>
      </div>
    </li>
    <li class="service service--training">
      <svg class="service-icon" viewBox="0 0 74 74" aria-hidden="true">
        <circle cx="37" cy="37" r="37" fill="var(--orange)"/>
        <path d="M40 22 H24 V52 H52 V36" fill="none" stroke="var(--white)" stroke-width="3" stroke-linejoin="round"/>
        <path d="M34 42 L36 36 L50 22 L54 26 L40 40 Z" fill="var(--white)"/>
      </svg>
      <div>
        <h2 class="service-title">Schulungen</h2>
        <p class="service-text">Eigenes IT-Forschungslabor zur Kompetenzsicherung</p>
      </div>
    </li>
  </ul>

  <div class="brand"><span class="brand-dot"></span>Veltrasec</div>

  <footer class="footer">
    <p class="footer-copy">Copyright text here</p>
  </footer>
</main>
</body>
</html>
```